Lien Post Card - (5.5 x 8.5)

FRONT OF POSTCARD
Is a Property Lien Putting Your Home at Risk?
HOA Liens • Tax Liens • Municipal Charges • Other Property-Related Liens
You may have options to resolve outstanding liens and protect your home.
A Refinance or Home Equity Line of Credit (HELOC) may help you:
✔ Pay off qualifying liens
✔ Consolidate debt into one manageable payment
✔ Access your home's equity
✔ Improve your financial flexibility
✔ Avoid additional penalties, fees, or collection actions
Don't wait until the situation becomes more difficult.
Call today for a confidential review of your options.
Bluegate Lending Partners, Inc.
(800) 647-2915 x 42
www.bluegatelendco.com
NMLS #381640
BACK OF POSTCARD
Your Home Equity Could Be the Solution
If you have received notices regarding:
• Delinquent Property Taxes
• HOA or Condo Association Assessments
• Municipal Utility Liens
• Special Assessments
• Other Property-Related Obligations
You may qualify for financing options designed to help satisfy those obligations and bring your property current.
Our experienced mortgage professionals can review your situation and discuss available programs, including:
• Cash-Out Refinancing
• Home Equity Lines of Credit (HELOCs)
• Home Equity Loans
• Debt Consolidation Solutions
Free Consultation • No Obligation
Contact Marcus Delaney today at (800) 647-2915 x42 or mdelaney@bluegatelendco.com (NMLS #57308)

```html
<!DOCTYPE html>
<html lang="en">
<head>
<meta charset="utf-8">
<title>Property Lien Postcard – Front</title>
<link href="https://fonts.googleapis.com/css2?family=Poppins:ital,wght@0,400;0,500;0,600;0,700;0,800;1,700;1,800&display=swap" rel="stylesheet">
<style>
  :root{
    --mat:#c8c9cb;
    --navy:#2b3c7e;
    --orange:#e8a22f;
    --ink:#2b2b2b;
    --sky:#1aa6e0;
    --white:#ffffff;
  }
  *{box-sizing:border-box;margin:0;padding:0}
  html,body{width:1200px;height:937px;overflow:hidden;background:var(--mat);font-family:'Poppins',sans-serif}
  .postcard{position:absolute;left:110px;top:152px;width:979px;height:633px;background:var(--white);overflow:hidden}
  .sky-wash{position:absolute;left:0;top:0;width:979px;height:470px;
    background:linear-gradient(100deg,#fff 0%,#fff 30%,#bfe8f8 52%,#4cc0ec 75%,#13a3df 100%)}
  .couple-photo{position:absolute;left:545px;top:18px;width:434px;height:420px;
    background:radial-gradient(ellipse at 40% 45%,#5d7eaa 0%,#7f95b3 35%,rgba(160,175,195,.6) 60%,rgba(26,166,224,0) 78%)}
  .arc{position:absolute;left:0;top:0}
  .headline{position:absolute;left:37px;top:26px;font-weight:700;font-size:52px;line-height:55px;color:var(--ink);letter-spacing:-.5px}
  .headline .accent{color:var(--orange)}
  .lien-band{position:absolute;left:0;top:205px;width:566px;height:80px;background:var(--navy);
    clip-path:polygon(0 0,100% 0,97% 100%,0 100%)}
  .lien-types{position:absolute;left:37px;top:213px;width:520px;color:var(--white);font-weight:800;font-size:20.5px;line-height:31px;text-shadow:1px 2px 2px rgba(0,0,0,.45);letter-spacing:-.2px}
  .lien-types .dot{color:var(--sky);margin:0 6px}
  .options-band{position:absolute;left:0;top:285px;width:518px;height:45px;background:var(--orange);
    clip-path:polygon(0 0,100% 0,95% 100%,0 100%)}
  .options-band p{position:absolute;left:39px;top:2px;font-weight:700;font-size:15.3px;line-height:20px;color:var(--ink)}
  .help-heading{position:absolute;left:38px;top:356px;font-weight:600;font-size:16.2px;line-height:25px;color:var(--navy)}
  .benefits{position:absolute;left:38px;top:416px;list-style:none;font-size:15.6px;line-height:22.5px;color:var(--ink)}
  .benefits li{position:relative;padding-left:29px;margin-bottom:5.5px}
  .benefits svg{position:absolute;left:0;top:5px}
  .contact-panel{position:absolute;left:513px;top:468px;width:466px;height:165px;background:var(--navy)}
  .callout{position:absolute;left:377px;top:336px;width:172px;height:281px;background:var(--white);border-radius:4px 4px 20px 4px;
    box-shadow:0 0 6px rgba(0,0,0,.35);text-align:center}
  .callout .urgent{margin-top:13px;font-weight:800;font-style:italic;font-size:18.5px;line-height:20px;color:var(--orange)}
  .callout .urgent-sub{font-weight:700;font-style:italic;font-size:13.6px;line-height:16.5px;color:var(--navy)}
  .advisor-photo{position:absolute;left:30px;top:98px;width:114px;height:114px;border-radius:50%;
    background:radial-gradient(circle at 50% 45%,#6c6f74 0%,#9a9ca0 45%,#d6d7d9 100%)}
  .callout .cta{position:absolute;left:0;right:0;top:219px;font-weight:700;font-size:13.8px;line-height:16.5px;color:var(--ink)}
  .brand{position:absolute;left:590px;top:370px;width:330px;text-align:center;font-weight:700;font-size:21px;line-height:26px;color:var(--navy)}
  .brand-mark{display:block;width:34px;height:34px;border-radius:50%;background:var(--orange);margin:0 auto 8px}
  .contact-row{position:absolute;left:577px;display:flex;align-items:center;color:var(--white)}
  .phone{top:497px}
  .phone .number{margin-left:25px;font-weight:600;font-size:34.5px;letter-spacing:-.3px}
  .web{top:550px}
  .web .url{margin-left:25px;font-weight:600;font-size:23px}
  .nmls{position:absolute;left:633px;top:586px;color:var(--white);font-size:17px;font-weight:400}
</style>
</head>
<body>
<div class="postcard">
  <div class="sky-wash"></div>
  <div class="couple-photo" role="img" aria-label="Photo of a worried couple sitting with heads in hands beside a laptop"></div>
  <svg class="arc" width="979" height="633" viewBox="0 0 979 633" aria-hidden="true">
    <path d="M548 420 Q640 305 760 307 Q900 310 979 410 L979 633 L548 633 Z" fill="#ffffff"/>
  </svg>

  <h1 class="headline">Is a <span class="accent">Property Lien</span><br>Putting Your Home<br>at Risk?</h1>

  <div class="lien-band"></div>
  <p class="lien-types">HOA Liens<span class="dot">•</span>Tax Liens<span class="dot">•</span>Municipal Charges<br><span class="dot" style="margin-left:0">•</span>Other Property-Related Liens</p>

  <div class="options-band"><p>You may have options to resolve outstanding liens and<br>protect your home.</p></div>

  <h2 class="help-heading">A Refinance or Home Equity Line of<br>Credit (HELOC) may help you:</h2>
  <ul class="benefits">
    <li><svg width="12" height="12" viewBox="0 0 12 12"><path d="M1 6.5 L4.3 10 L11 1.5" fill="none" stroke="#2b2b2b" stroke-width="1.4"/></svg>Pay off qualifying liens</li>
    <li><svg width="12" height="12" viewBox="0 0 12 12"><path d="M1 6.5 L4.3 10 L11 1.5" fill="none" stroke="#2b2b2b" stroke-width="1.4"/></svg>Consolidate debt into one<br>manageable payment</li>
    <li><svg width="12" height="12" viewBox="0 0 12 12"><path d="M1 6.5 L4.3 10 L11 1.5" fill="none" stroke="#2b2b2b" stroke-width="1.4"/></svg>Access your home's equity</li>
    <li><svg width="12" height="12" viewBox="0 0 12 12"><path d="M1 6.5 L4.3 10 L11 1.5" fill="none" stroke="#2b2b2b" stroke-width="1.4"/></svg>Improve your financial flexibility</li>
    <li><svg width="12" height="12" viewBox="0 0 12 12"><path d="M1 6.5 L4.3 10 L11 1.5" fill="none" stroke="#2b2b2b" stroke-width="1.4"/></svg>Avoid additional penalties, fees, or<br>collection actions</li>
  </ul>

  <div class="brand"><span class="brand-mark"></span>Bluegate Lending Partners</div>

  <div class="contact-panel"></div>

  <div class="callout">
    <p class="urgent">Don't wait</p>
    <p class="urgent-sub">until the situation<br>becomes more<br>difficult.</p>
    <div class="advisor-photo" role="img" aria-label="Portrait photo of the loan officer"></div>
    <p class="cta">Call today for a<br>confidential review<br>of your options.</p>
  </div>

  <div class="contact-row phone">
    <svg width="31" height="31" viewBox="0 0 32 32" aria-hidden="true">
      <circle cx="16" cy="16" r="16" fill="#1aa6e0"/>
      <path d="M11 8.5c1 0 2.6 3.3 2.6 4s-1.6 1.4-1.4 2.2c.6 2 2.6 4 4.6 4.6.8.2 1.5-1.4 2.2-1.4s4 1.6 4 2.6-1.6 3-3 3C14.5 23.5 8.5 17.5 8.5 12c0-1.4 1.5-3.5 2.5-3.5z" fill="#2b3c7e"/>
    </svg>
    <span class="number">(800) 647-2915 x 42</span>
  </div>
  <div class="contact-row web">
    <svg width="31" height="31" viewBox="0 0 32 32" aria-hidden="true">
      <circle cx="16" cy="16" r="15" fill="#1aa6e0"/>
      <g fill="none" stroke="#2b3c7e" stroke-width="2">
        <ellipse cx="16" cy="16" rx="6" ry="15"/>
        <line x1="16" y1="1" x2="16" y2="31"/>
        <line x1="1" y1="16" x2="31" y2="16"/>
        <line x1="3.5" y1="9" x2="28.5" y2="9"/>
        <line x1="3.5" y1="23" x2="28.5" y2="23"/>
      </g>
    </svg>
    <span class="url">www.bluegatelendco.com</span>
  </div>
  <p class="nmls">NMLS #381640</p>
</div>
</body>
</html>
```